Harborlight havens a space of healing for first responders veterans and caregivers.

Build a complete website for Harborlight Havens, a wellness and retreat company focused on first responders, caregivers, veterans, and individuals navigating PTSD, depression, anxiety, and burnout.

Style & Branding:

Blend American pride (strong, grounded, resilient) with feminine & masculine balance (warmth, nurturing, strength).

Incorporate imagery of fire, light, and renewal (aligned with Harborlight Havens’ logo and flame theme).

Use colors that reflect trust, healing, and vitality: deep blues/greens for calm, earthy tones for grounding, fire-inspired accents (gold/orange/red) for resilience.

Clean, modern layout that feels sacred yet professional, approachable but inspiring.

Homepage:

Hero section with a bold headline: “Harborlight Havens – Healing and Resilience for Frontline Warriors”.

Background image: people gathered around a retreat fire circle or blended visuals of first responders & nature.

Call-to-Action buttons:

“Book a Nervous System Blueprint Call” (Calendly integration).

“Take the Free Nervous System Quiz” (Jotform or embedded form).

Features & Pages:

Upcoming Retreats Page

Pull in graphics/photos from current website or provided assets.

Highlight retreat details: dates, location, themes (somatics, yoga, breathwork, psychedelic integration, resilience training).

Easy booking option (linked to Calendly or built-in checkout).

Programs & Coaching

Nervous System Blueprint Call booking (Calendly).

Coaching services (mental health, somatic healing, integrative practices).

Workshop offers for businesses/organizations to increase productivity and resilience.

Free Resource Lead Magnet

“Take the Nervous System Quiz” → Auto-email delivery of free Somatics Healing Book (PDF).

Clear funnel integration: quiz → email capture → deliver PDF → upsell to retreats or calls.

About Page

Founder bio: Marisa Holbrook – Retired firefighter (14 years), trauma-informed resiliency coach, founder of Harborlight Havens. Speaker kit included for reference of get to know mr and the subjects i speak on professionally as a paid speaker.

Story of transformation from PTSD and frontline burnout → mission to help others heal.

Healing Modalities Page

Somatics, yoga, breathwork, psychedelic-assisted healing, integrative retreats.

Explain how these practices restore nervous system balance, resilience, and purpose.

Contact Page

Direct email & phone.

Embedded chat option if available.

Functionality:

Calendly integration for retreat calls, coaching sessions, and workshops.

E-commerce capability to sell books, PDFs, and courses (Coursebox or integrated Shopify/Stripe).

SEO optimized with keywords: PTSD healing retreats, resilience coaching, somatics workshops, nervous system reset, first responder retreats, caregiver healing, veteran wellness.

Mobile-optimized for easy scheduling and access.

Tone & Messaging:

Empathetic, authentic, and encouraging.

Balance between professional mental health support and personal lived experience.

Messaging to emphasize: “You are not alone. Healing is possible. Rekindle your strength and resilience.”

Target Market(s)

men and women on the frontlines caregivers veterans first responders

Industry/Entity Type

wellness, first responders

Coding

Coded - Design and coding required

Number of Pages Required

1 page

Requirements
Must have
• first responder blend with holistic nature relaxation vibes. clear link to jotform quiz, calendly book your custom blue print phone call
Nice to have
• integrated about me and my business partner page messaging around psylocibin mdma medicine journies such as Quiet Harbor Gathering Summit Path Gathering Tending the Roots Widening Horizons Gathering The Still Meadow Cedar Trail Restoration
Should not have
• mention of psilocybin directly, mention licensed therapist or other licensing

```html
<!DOCTYPE html>
<html lang="en">
<head>
<meta charset="utf-8">
<title>Harborlight Havens – Healing and Resilience for Frontline Warriors</title>
<link rel="stylesheet" href="https://fonts.googleapis.com/css2?family=Poppins:wght@300;400;500;600;700&family=Playfair+Display:ital@1&display=swap">
<style>
:root{
  --ember:#e9672a;
  --ember-deep:#d9551e;
  --crimson:#b7282e;
  --crimson-dark:#8e1d24;
  --gold:#f1b130;
  --paper:#f1efec;
  --ink:#1d1d1d;
  --white:#ffffff;
  --night:#2d3236;
  --footer-bar:#3b1c1c;
}
*{margin:0;padding:0;box-sizing:border-box}
html,body{width:1200px;height:3712px;overflow:hidden}
body{font-family:"Poppins",sans-serif;color:var(--ink);background:var(--paper);position:relative}
.section{position:absolute;left:0;width:1200px;overflow:hidden}
.abs{position:absolute}
.center{text-align:center}

/* hero */
.hero{top:0;height:631px;background:linear-gradient(180deg,#8a6a58 0%,#d98a4c 35%,#f29a50 60%,#e6813d 100%)}
.logo{position:absolute;border-radius:50%;background:var(--crimson);display:flex;align-items:center;justify-content:center;text-align:center;color:var(--white);font-weight:600;line-height:1.2}
.hero .logo{left:144px;top:10px;width:116px;height:116px;font-size:13px;border:4px solid var(--gold)}
.nav{position:absolute;left:358px;top:30px;display:flex;gap:34px;font-size:18px;color:var(--white)}
.follow{position:absolute;left:862px;top:32px;font-size:13px;color:var(--white)}
.social{position:absolute;top:26px;width:32px;height:32px;border-radius:50%;background:var(--white);border:2px solid rgba(255,255,255,.6)}
.hero-photo{position:absolute;left:605px;top:86px;width:505px;height:545px;border-radius:200px 200px 0 0;background:linear-gradient(180deg,#3a3f4a 0%,#2b2f38 55%,#c8b24a 100%);opacity:.92}
.hero-kicker{left:140px;top:218px;font-size:34px;font-weight:400;color:var(--white)}
.hero-title{left:140px;top:264px;font-size:33px;font-weight:700;color:var(--white);line-height:40px}
.btn{position:absolute;display:flex;align-items:center;justify-content:center;border-radius:24px;font-weight:600;font-size:14px;color:var(--white)}
.btn-red{left:144px;top:357px;width:369px;height:46px;background:var(--crimson)}
.btn-orange{left:144px;top:413px;width:369px;height:46px;background:var(--ember-deep)}
.play-line{left:0;top:552px;width:140px;height:2px;background:var(--white)}
.play{left:138px;top:528px;width:50px;height:50px;border-radius:50%;border:3px solid var(--white);background:rgba(255,255,255,.15);display:flex;align-items:center;justify-content:center}
.play span{width:30px;height:30px;border-radius:50%;background:var(--white);display:flex;align-items:center;justify-content:center}
.play-label{left:201px;top:542px;font-size:14px;color:var(--white)}

/* band */
.band{top:631px;height:75px;background:linear-gradient(90deg,var(--ember) 0%,var(--crimson) 100%)}
.band-text{left:143px;top:23px;font-size:20px;color:var(--white)}
.band-text b{font-weight:700}
.band-btn{left:778px;top:17px;width:277px;height:40px;border-radius:22px;background:var(--white);color:var(--ink);font-size:12px;font-weight:700;display:flex;align-items:center;justify-content:center}

/* understand */
.understand{top:706px;height:749px;background:var(--paper)}
.h2{font-size:36px;line-height:40px;color:var(--ink);font-weight:400}
.h2 b{font-weight:700}
.understand .h2{left:0;width:1200px;top:62px}
.lead{font-size:16.5px;line-height:24px}
.understand .lead{left:200px;width:800px;top:194px}
.photo{position:absolute;top:319px;height:330px;width:277px}
.photo-a{left:144px;border-radius:140px 0 0 0;border-top:6px solid var(--ember);background:linear-gradient(160deg,#5a4538,#8a6b55 60%,#2b2a2e)}
.photo-b{left:461px;border-radius:0 0 140px 140px;border-bottom:6px solid var(--ember);background:linear-gradient(160deg,#b9b7b5,#3b3d46 60%,#c23a2c)}
.photo-c{left:779px;border-radius:140px 140px 0 0;border-top:6px solid var(--ember);background:linear-gradient(160deg,#8d8f92,#3a3d40 55%,#c7b544)}

/* welcome */
.welcome{top:1455px;height:557px;background:linear-gradient(180deg,#3b4145 0%,#505355 45%,#7a5b44 70%,#2a2a2a 100%)}
.welcome .h2{left:0;width:1200px;top:146px;color:var(--white);font-size:35px}
.welcome .lead{left:230px;width:740px;top:248px;color:var(--white)}

/* offerings */
.offerings{top:2012px;height:701px;background:var(--ember)}
.offerings .h2{left:0;width:1200px;top:72px;color:var(--white)}
.arch{position:absolute;top:141px;width:368px;height:427px;border-radius:184px 184px 0 0;background:var(--white);padding:10px 8px 0}
.arch div{width:100%;height:100%;border-radius:176px 176px 0 0}
.arch-a{left:184px}
.arch-a div{background:linear-gradient(180deg,#f5f2ee,#e8c8b6 60%,#d9b39a)}
.arch-b{left:648px}
.arch-b div{background:linear-gradient(180deg,#cfd4d8,#b9a89a 55%,#6d6e72)}
.label{position:absolute;top:2518px;width:275px;height:82px;background:var(--white);display:flex;align-items:center;justify-content:center;text-align:center;font-size:20px;font-weight:500;line-height:28px;top:518px}
.label-a{left:235px}
.label-b{left:691px}
.chev{position:absolute;top:340px}

/* testimonial */
.testimonial{top:2713px;height:595px;background:var(--paper)}
.t-photo{left:131px;top:110px;width:372px;height:372px;border-radius:50%;background:linear-gradient(180deg,#d3dde2 0%,#7d97a6 50%,#c2a57e 100%)}
.t-arc{left:100px;top:80px}
.t-title{left:514px;width:600px;top:135px;font-size:32px;letter-spacing:.5px;color:var(--ink)}
.t-title b{font-weight:700}
.t-quote-mark{left:785px;top:205px;font-family:"Playfair Display",serif;font-size:110px;line-height:100px;color:var(--ember)}
.t-text{left:620px;width:390px;top:287px;font-family:"Playfair Display",serif;font-style:italic;font-size:14.5px;line-height:24px;color:#444}
.t-arrow{position:absolute;top:3060px;width:36px;height:36px;border-radius:50%;background:var(--crimson);display:flex;align-items:center;justify-content:center;top:347px}
.avatar{left:733px;top:418px;width:66px;height:66px;border-radius:50%;background:linear-gradient(180deg,#c9ccd0,#6b5b51)}
.t-name{left:812px;top:430px;font-size:18px;font-weight:600}
.t-role{left:812px;top:456px;font-size:14px;color:#444}

/* footer */
.footer{top:3308px;height:340px;background:linear-gradient(180deg,#c0302c 0%,#b32426 60%,#9b1e22 100%)}
.footer .logo{left:165px;top:81px;width:142px;height:142px;font-size:16px;border:5px solid #f3d7c8}
.f-social{position:absolute;top:247px;width:34px;height:34px;border-radius:50%;border:2px solid var(--white)}
.f-head{position:absolute;top:90px;font-size:20px;font-weight:600;color:var(--white);letter-spacing:.3px}
.f-links{position:absolute;left:393px;top:132px;list-style:none;font-size:14px;color:var(--white);line-height:24px}
.f-links li::before{content:"";display:inline-block;width:8px;height:8px;border-radius:50%;background:var(--gold);margin-right:15px;vertical-align:1px}
.f-item{position:absolute;left:585px;font-size:14px;color:var(--white);line-height:21px}
.f-item b{font-weight:600}
.f-icon{position:absolute;left:-24px;top:2px}
.f-email{left:815px;top:126px;width:245px;height:38px;border-radius:20px;background:rgba(255,255,255,.18);color:var(--white);font-size:14px;display:flex;align-items:center;padding-left:40px}
.f-sub{left:815px;top:174px;width:125px;height:38px;border-radius:20px;background:var(--gold);font-size:14px;font-weight:600;display:flex;align-items:center;justify-content:center;color:var(--ink)}
.bottom{top:3648px;height:64px;background:var(--footer-bar);color:var(--white);font-size:14px;display:flex;align-items:center;justify-content:center}
</style>
</head>
<body>

<section class="section hero">
  <div class="logo">HARBORLIGHT<br>HAVENS</div>
  <nav class="nav"><span>Home</span><span>Features</span><span>About Us</span><span>Blog</span><span>Contact</span></nav>
  <div class="follow">Follow Us :</div>
  <div class="social" style="left:943px" aria-label="Social link"></div>
  <div class="social" style="left:984px" aria-label="Social link"></div>
  <div class="social" style="left:1024px" aria-label="Social link"></div>
  <div class="hero-photo" role="img" aria-label="Smiling firefighter in helmet and turnout gear against a sunset sky"></div>
  <div class="abs hero-kicker">Harborlight Havens</div>
  <h1 class="abs hero-title">Healing and Resilience for<br>Frontline Warriors</h1>
  <a class="btn btn-red">BOOK A NERVOUS SYSTEM BLUEPRINT CALL</a>
  <a class="btn btn-orange">TAKE THE FREE NERVOUS SYSTEM QUIZ</a>
  <div class="abs play-line"></div>
  <div class="abs play"><span><svg width="12" height="14" viewBox="0 0 12 14"><path d="M1 1l10 6-10 6z" fill="#e9672a"/></svg></span></div>
  <div class="abs play-label">Play Now</div>
</section>

<section class="section band">
  <div class="abs band-text">Your Path to Transformation: <b>Find Your Perfect Program.</b></div>
  <a class="abs band-btn">VIEW ALL RETREATS &amp; WORKSHOPS</a>
</section>

<section class="section understand">
  <h2 class="abs h2 center"><b>At Harborlight Havens, We Understand</b><br><b>The Profound</b> Impact That Stress And Trauma<br>Can Have On Your Life.</h2>
  <p class="abs lead center">That's why we focus on powerful modalities like nervous system regulation, somatic healing, and inner resilience. Our programs integrate breathwork, parts work (IFS-inspired), trauma timeline rewriting, hot/cold therapy, yoga, and mindfulness practices to offer a holistic path to recovery.</p>
  <div class="photo photo-a" role="img" aria-label="Close-up of a firefighter's weathered hands on a turnout coat"></div>
  <div class="photo photo-b" role="img" aria-label="Laughing firefighter in helmet beside an ambulance"></div>
  <div class="photo photo-c" role="img" aria-label="Firefighter carrying a ladder beside a fire truck"></div>
</section>

<section class="section welcome" role="img" aria-label="Person holding a yoga pose on a wooden dock over the sea at dusk">
  <h2 class="abs h2 center"><b>Welcome To Harborlight Havens,</b><br>A Sanctuary For Healing And Renewal.</h2>
  <div class="abs lead center">
    <p>We are a trauma-informed wellness company dedicated to helping individuals recover from burnout, trauma, and major life transitions. Our immersive retreats, workshops, and one-on-one coaching are designed to guide you back to a place of grounding, self-reconnection, clarity, and purpose.</p>
    <p style="margin-top:24px">We understand the unique and profound toll of a life spent in service, and our programs are a direct response to that need.</p>
  </div>
</section>

<section class="section offerings">
  <h2 class="abs h2 center"><b>Discover Our</b> Upcoming Offerings.</h2>
  <svg class="chev" style="left:60px" width="24" height="44" viewBox="0 0 24 44"><path d="M21 3L4 22l17 19" fill="none" stroke="#fff" stroke-width="3"/></svg>
  <svg class="chev" style="left:1116px" width="24" height="44" viewBox="0 0 24 44"><path d="M3 3l17 19L3 41" fill="none" stroke="#fff" stroke-width="3"/></svg>
  <div class="arch arch-a"><div role="img" aria-label="Woman in a flowing dress turning toward the sun"></div></div>
  <div class="arch arch-b"><div role="img" aria-label="Two people in conversation during a workshop"></div></div>
  <div class="label label-a">Harborlight Retrieval<br>Retreats</div>
  <div class="label label-b">Deep Dive<br>Workshops</div>
</section>

<section class="section testimonial">
  <svg class="abs t-arc" width="440" height="440" viewBox="0 0 440 440"><path d="M212 6 A214 214 0 0 1 212 434" fill="none" stroke="#b7282e" stroke-width="14"/></svg>
  <div class="abs t-photo" role="img" aria-label="Woman in meditation pose overlooking a calm lake and hills"></div>
  <h2 class="abs t-title center"><b>WHAT OUR</b> CLIENTS SAY</h2>
  <div class="abs t-quote-mark">&ldquo;</div>
  <p class="abs t-text center">"After years of carrying the weight of my profession, Harborlight Havens offered me a true sanctuary. The somatic work and nervous system regulation practices were exactly what I needed to finally feel grounded again. I'm returning to my life with a clarity I haven't felt in years."</p>
  <div class="t-arrow" style="left:559px"><svg width="10" height="14" viewBox="0 0 10 14"><path d="M8 1L2 7l6 6" fill="none" stroke="#fff" stroke-width="2"/></svg></div>
  <div class="t-arrow" style="left:1033px"><svg width="10" height="14" viewBox="0 0 10 14"><path d="M2 1l6 6-6 6" fill="none" stroke="#fff" stroke-width="2"/></svg></div>
  <div class="abs avatar" role="img" aria-label="Client portrait"></div>
  <div class="abs t-name">J. Marlowe</div>
  <div class="abs t-role">First Responder</div>
</section>

<footer class="section footer">
  <div class="logo">HARBORLIGHT<br>HAVENS</div>
  <div class="f-social" style="left:175px" aria-label="Social link"></div>
  <div class="f-social" style="left:215px;background:var(--gold);border-color:var(--gold)" aria-label="Social link"></div>
  <div class="f-social" style="left:255px" aria-label="Social link"></div>

  <div class="f-head" style="left:393px">QUICK LINKS</div>
  <ul class="f-links"><li>Home</li><li>About us</li><li>Features</li><li>Blog</li><li>Reviews</li><li>FAQ</li><li>Contact us</li></ul>

  <div class="f-head" style="left:585px">CONTACT US</div>
  <div class="f-item" style="top:128px"><svg class="f-icon" width="12" height="16" viewBox="0 0 12 16"><path d="M6 0a6 6 0 0 0-6 6c0 4.5 6 10 6 10s6-5.5 6-10a6 6 0 0 0-6-6zm0 8.5A2.5 2.5 0 1 1 6 3.5a2.5 2.5 0 0 1 0 5z" fill="#f1b130"/></svg><b>Address :</b><br>12 Beacon Cove Road</div>
  <div class="f-item" style="top:192px"><svg class="f-icon" width="14" height="14" viewBox="0 0 14 14"><path d="M3 0l3 3-2 2a9 9 0 0 0 5 5l2-2 3 3-2 3C6 14 0 8 0 2z" fill="#f1b130"/></svg><b>Phone :</b><br>+1 555 014 2290</div>
  <div class="f-item" style="top:256px"><svg class="f-icon" width="15" height="11" viewBox="0 0 15 11"><rect width="15" height="11" rx="1" fill="#f1b130"/><path d="M1 1l6.5 5L14 1" fill="none" stroke="#b32426" stroke-width="1.4"/></svg><b>Email Address :</b><br>hello@harborlighthavens.example</div>

  <div class="f-head" style="left:815px">OUR NEWSLETTER</div>
  <div class="abs f-email"><svg style="position:absolute;left:15px" width="15" height="11" viewBox="0 0 15 11"><rect width="15" height="11" rx="1" fill="#fff"/><path d="M1 1l6.5 5L14 1" fill="none" stroke="#b32426" stroke-width="1.4"/></svg>Email address</div>
  <div class="abs f-sub">SUBSCRIBE</div>
</footer>

<div class="section bottom">&copy;&nbsp; Copyrights 2025 | All Rights Reserved</div>

</body>
</html>
```